NEW Inspirational Young Adults Book Needs Cover Design

The title of the book is:
The Lantern and the Kite: Notes on Money, Friends, Cities, Music, and Courage in Early Life
This a short book and I imagine A5 in size. Needs to be funky and appealing for the 15-25 age group. I have always imagined it some how featuring a frog and a fish. I have attached the contents and a page of the intro to show how the frog and fish fit with the book.

Target Market(s)

Young adults 15-25 years age

Industry/Entity Type

Education

Font styles to use
Sans Serif

Requirements
Must have
• a frog and a fish

```html
<!DOCTYPE html>
<html lang="en">
<head>
<meta charset="utf-8">
<title>The Lantern and the Kite – Book Cover</title>
<link rel="stylesheet" href="https://fonts.googleapis.com/css2?family=Open+Sans:wght@400;700;800&display=swap">
<style>
  :root{
    --sky-deep:#2f8fd2;
    --sky-mid:#5fb3e6;
    --sky-pale:#dcefFa;
    --banner:#1f7fc4;
    --banner-dark:#176aa8;
    --orange:#f6a020;
    --orange-deep:#d9731a;
    --cloud:#cfe8f8;
    --crowd:#1c1c1c;
    --frog:#f4c72e;
    --fish:#1f84a6;
    --ink:#4a5560;
    --white:#ffffff;
    --stage:#ececec;
  }
  *{box-sizing:border-box;margin:0;padding:0}
  html,body{width:1200px;height:1200px;overflow:hidden;background:var(--stage);font-family:"Open Sans",sans-serif}
  .wrap-spread{position:absolute;left:50px;top:232px;width:1100px;height:735px;display:flex;box-shadow:0 18px 40px rgba(0,0,0,.18)}
  .panel{position:relative;height:100%;overflow:hidden;background:linear-gradient(180deg,var(--sky-deep) 0%,var(--sky-mid) 45%,var(--sky-pale) 100%)}
  .back-cover,.front-cover{width:520px}
  .spine{width:60px;background:linear-gradient(180deg,var(--sky-deep) 0%,var(--sky-mid) 100%)}
  .shapes{position:absolute;inset:0;width:100%;height:100%}
  .art{position:absolute}

  /* front */
  .title-block{position:absolute;left:70px;top:360px;width:400px;transform:rotate(-10deg);transform-origin:left top;color:var(--white)}
  .title-line{font-weight:800;line-height:.95;letter-spacing:-1px;white-space:nowrap}
  .title-the{font-size:34px}
  .title-main{font-size:60px}
  .title-and{font-size:34px;padding-left:120px}
  .title-kite{padding-left:80px}
  .subtitle{margin-top:8px;font-size:15px;line-height:1.3;font-weight:400;white-space:nowrap}
  .author{position:absolute;left:110px;top:702px;width:320px;display:flex;align-items:center;gap:10px;transform:rotate(-10deg);transform-origin:left top;color:var(--ink);font-size:18px;line-height:1.2;letter-spacing:2px;white-space:nowrap}
  .author::before,.author::after{content:"";flex:1;height:2px;background:var(--ink)}

  /* spine */
  .spine-band{position:absolute;left:0;top:130px;width:60px;height:440px;background:var(--orange)}
  .spine-title{position:absolute;left:30px;top:150px;writing-mode:vertical-rl;transform:translateX(-50%);color:var(--white);font-weight:800;font-size:18px;white-space:nowrap}
  .spine-author{position:absolute;left:30px;top:595px;writing-mode:vertical-rl;transform:translateX(-50%);color:var(--ink);font-size:12px;letter-spacing:2px;white-space:nowrap}

  /* back */
  .blurb{position:absolute;left:60px;top:150px;width:410px;transform:rotate(4deg);transform-origin:left top;color:var(--white);font-size:15px;line-height:1.62;text-align:center;font-weight:700}
  .blurb p{margin-bottom:6px}
</style>
</head>
<body>
<main class="wrap-spread">

  <section class="panel back-cover">
    <svg class="shapes" viewBox="0 0 520 735" aria-hidden="true">
      <defs>
        <linearGradient id="backOrange" x1="0" y1="1" x2="1" y2="0">
          <stop offset="0" stop-color="#cf6418"/><stop offset="1" stop-color="#f8a828"/>
        </linearGradient>
      </defs>
      <polygon points="50,570 90,655 110,560" fill="var(--banner)"/>
      <polygon points="40,120 520,110 520,520 30,580" fill="url(#backOrange)"/>
    </svg>
    <div class="art" role="img" aria-label="Soft white clouds in the sky" style="left:40px;top:40px;width:150px;height:85px;border-radius:45px;background:var(--cloud)"></div>
    <div class="art" role="img" aria-label="Small cloud" style="left:400px;top:55px;width:70px;height:35px;border-radius:20px;background:var(--cloud)"></div>
    <div class="blurb">
      <p>Lorem ipsum dolor sit amet, consectetuer adipiscing elit. Aenean commodo ligula eget dolor. Aenean massa. Cum sociis natoque penatibus et magnis dis parturient montes, nascetur ridiculus mus. Donec quam felis.</p>
      <p>Nulla consequat massa quis enim. Donec pede justo, fringilla vel, aliquet nec, vulputate eget, arcu. In enim justo, rhoncus ut, imperdiet a, venenatis vitae, justo. Nullam dictum felis eu pede mollis pretium.</p>
      <p>Vivamus elementum semper nisi. Aenean vulputate eleifend tellus. Aenean leo ligula, porttitor eu, consequat vitae, eleifend ac, enim. Nullam quis ante. Etiam sit amet orci eget eros faucibus tincidunt. Duis leo. Sed fringilla mauris sit amet nibh.</p>
    </div>
    <div class="art" role="img" aria-label="Yellow origami frog" style="left:150px;top:600px;width:120px;height:80px;border-radius:12px;background:linear-gradient(135deg,#f9d84a,var(--frog))"></div>
    <div class="art" role="img" aria-label="Teal origami fish" style="left:290px;top:570px;width:120px;height:65px;border-radius:12px;background:linear-gradient(135deg,#2a9bbf,var(--fish))"></div>
  </section>

  <section class="panel spine">
    <div class="spine-band"></div>
    <div class="spine-title">The Lantern and The Kite</div>
    <div class="spine-author">AUTHOR NAME</div>
  </section>

  <section class="panel front-cover">
    <svg class="shapes" viewBox="0 0 520 735" aria-hidden="true">
      <defs>
        <linearGradient id="frontOrange" x1="0" y1="1" x2="1" y2="0">
          <stop offset="0" stop-color="var(--orange-deep)"/><stop offset="1" stop-color="var(--orange)"/>
        </linearGradient>
        <linearGradient id="bannerFill" x1="0" y1="0" x2="1" y2="1">
          <stop offset="0" stop-color="var(--banner)"/><stop offset="1" stop-color="var(--banner-dark)"/>
        </linearGradient>
      </defs>
      <polygon points="0,105 520,190 520,300 60,560 0,540" fill="url(#frontOrange)"/>
      <polygon points="175,580 210,640 230,565" fill="var(--orange)"/>
      <polygon points="30,345 505,265 470,520 90,610" fill="url(#bannerFill)"/>
    </svg>
    <div class="art" role="img" aria-label="Clouds in a blue sky" style="left:30px;top:55px;width:90px;height:50px;border-radius:25px;background:var(--cloud)"></div>
    <div class="art" role="img" aria-label="Small cloud" style="left:430px;top:40px;width:75px;height:45px;border-radius:22px;background:var(--cloud)"></div>
    <div class="art" role="img" aria-label="Silhouette of graduates cheering and throwing caps into the air" style="left:30px;top:60px;width:460px;height:240px;clip-path:polygon(0 100%,0 55%,20% 40%,35% 20%,55% 0,75% 15%,92% 30%,100% 60%,100% 75%);background:linear-gradient(180deg,#3a3a3a,var(--crowd))"></div>
    <div class="title-block">
      <div class="title-line"><span class="title-the">THE </span><span class="title-main">LANTERN</span></div>
      <div class="title-line title-and">AND THE</div>
      <div class="title-line title-main title-kite">KITE</div>
      <div class="subtitle">Notes on Money, Friends, Cities, Music,<br>and Courage in Early Life</div>
    </div>
    <div class="art" role="img" aria-label="Teal origami fish" style="left:330px;top:540px;width:140px;height:60px;border-radius:14px;background:linear-gradient(135deg,#2a9bbf,var(--fish))"></div>
    <div class="art" role="img" aria-label="Yellow origami frog" style="left:110px;top:612px;width:150px;height:60px;border-radius:16px;background:linear-gradient(135deg,#fae06a,var(--frog))"></div>
    <div class="author">AUTHOR NAME</div>
  </section>

</main>
</body>
</html>
```